Urine collection cup with and without sterile seal sticker

Hello. We need a urine cup label designed please with

Name:
Date of Birth:
Date:
Time:
Temp℃:
Specimen ID:

Product code: TUB-47
Volume markings (e.g., 30 mL, 60 mL, 90 mL).
Vela Drug Tests logo

Could you please provide one version with the additional sterile sticker extending to the top, and one version without the additional sterile sticker?

```html
<!DOCTYPE html>
<html lang="en">
<head>
<meta charset="utf-8">
<title>Vela Drug Tests – Urine Cup Labels</title>
<link rel="stylesheet" href="https://fonts.googleapis.com/css2?family=Montserrat:wght@600;700;800&family=Inter:wght@400;500;600;700&display=swap">
<style>
  :root {
    --navy: #0f2b5b;
    --blue: #1f8fe0;
    --panel: #eef4fb;
    --rule: #1d2f55;
    --paper: #ffffff;
    --ink: #14284d;
  }
  * { box-sizing: border-box; margin: 0; padding: 0; }
  html, body { width: 1200px; height: 620px; overflow: hidden; background: var(--paper); }
  body { position: relative; font-family: "Inter", Arial, sans-serif; color: var(--ink); }

  .version-title {
    position: absolute; left: 0; width: 1200px; text-align: center;
    font-family: "Montserrat", Arial, sans-serif; font-weight: 700;
    font-size: 15px; letter-spacing: 0.6px; color: var(--navy);
  }
  .version-title.v1 { top: 11px; }
  .version-title.v2 { top: 298px; }

  .label {
    position: absolute; border: 1.6px solid var(--navy); border-radius: 11px;
    background: var(--paper); overflow: hidden;
  }
  .label.v1 { left: 23px; top: 36px; width: 929px; height: 240px; }
  .label.v2 { left: 23px; top: 321px; width: 1114px; height: 241px; }

  .brand { position: absolute; left: 36px; top: 80px; width: 310px; }
  .brand-row { display: flex; align-items: center; gap: 10px; }
  .brand-dot { width: 30px; height: 30px; border-radius: 50%; background: var(--blue); flex: none; }
  .brand-name {
    font-family: "Montserrat", Arial, sans-serif; font-weight: 800;
    font-size: 31px; line-height: 1; color: var(--navy); white-space: nowrap;
  }

  .divider { position: absolute; left: 356px; top: 20px; width: 1.4px; height: 164px; background: var(--rule); opacity: 0.7; }

  .patient-heading {
    position: absolute; left: 375px; top: 11px; height: 21px; padding: 0 11px;
    background: var(--navy); color: #fff; border-radius: 3px;
    font-family: "Montserrat", Arial, sans-serif; font-weight: 700; font-size: 14px;
    line-height: 21px; letter-spacing: 0.5px;
  }
  .field {
    position: absolute; left: 375px; display: flex; align-items: flex-end;
    font-weight: 600; font-size: 14px; line-height: 1;
  }
  .field .line { border-bottom: 1.1px solid var(--ink); height: 14px; margin-left: 5px; }
  .field.name { top: 46px; } .field.name .line { width: 344px; }
  .field.dob { top: 76px; } .field.dob .line { width: 296px; }
  .field.date { top: 108px; } .field.date .line { width: 157px; }
  .field.time { top: 108px; left: 594px; } .field.time .line { width: 133px; }
  .field.temp { top: 139px; } .field.temp .line { width: 330px; }
  .field.specimen { top: 169px; } .field.specimen .line { width: 296px; }

  .footer-rule { position: absolute; left: 0; top: 198px; height: 1px; background: var(--rule); opacity: 0.5; }
  .label.v1 .footer-rule { width: 804px; }
  .label.v2 .footer-rule { width: 797px; }

  .ref-box {
    position: absolute; left: 32px; top: 207px; width: 38px; height: 23px;
    border: 1.5px solid var(--navy); font-weight: 700; font-size: 14px;
    text-align: center; line-height: 20px; color: var(--navy);
  }
  .product-label { position: absolute; left: 84px; top: 212px; font-weight: 700; font-size: 11px; letter-spacing: 0.4px; color: var(--navy); }
  .product-code {
    position: absolute; left: 197px; top: 207px; width: 76px; height: 23px; border-radius: 4px;
    background: var(--navy); color: #fff; font-weight: 700; font-size: 15px; text-align: center; line-height: 23px;
  }
  .ivd-icon { position: absolute; left: 306px; top: 203px; width: 31px; height: 31px; }
  .ivd-text { position: absolute; left: 348px; top: 204px; font-size: 12.5px; line-height: 16px; color: var(--navy); }

  .volume-panel { position: absolute; top: 0; height: 100%; background: var(--panel); border-left: 1px solid rgba(29,47,85,0.5); }
  .label.v1 .volume-panel { left: 804px; width: 125px; }
  .label.v2 .volume-panel { left: 797px; width: 142px; }
  .volume-panel svg { position: absolute; left: 0; top: 0; }
  .vol { position: absolute; left: 58px; font-size: 19px; font-weight: 500; color: var(--navy); }
  .label.v2 .vol { left: 61px; }
  .vol small { font-size: 13px; }
  .vol.v90 { top: 13px; } .vol.v60 { top: 83px; } .vol.v30 { top: 154px; }

  .seal {
    position: absolute; left: 962px; top: 289px; width: 99px; height: 310px;
    background: var(--navy); border-radius: 14px; color: #fff; text-align: center;
    font-family: "Montserrat", Arial, sans-serif; font-weight: 800;
  }
  .seal::before, .seal::after {
    content: ""; position: absolute; top: 4px; bottom: 4px; width: 0;
    border-left: 1px dashed rgba(255,255,255,0.55);
  }
  .seal::before { left: 9px; } .seal::after { right: 9px; }
  .seal-icon { position: absolute; left: 34px; width: 31px; height: 31px; }
  .seal-icon.shield { top: 13px; }
  .seal-icon.lock { top: 246px; }
  .seal-word { position: absolute; left: 0; width: 100%; font-size: 13px; }
  .seal-word.sterile { top: 49px; }
  .seal-word.tamper { top: 280px; font-size: 11px; line-height: 14px; }
  .seal-band {
    position: absolute; left: 9px; top: 68px; width: 81px; height: 176px;
    background: #f3f6fa; border-left: 1px dashed #8a98b4; border-right: 1px dashed #8a98b4;
  }
  .seal-band svg { position: absolute; left: 0; top: 0; }
  .seal-warning {
    position: absolute; left: 40.5px; top: 88px; transform: translate(-50%, -50%) rotate(-90deg);
    white-space: nowrap; color: var(--navy); font-size: 14px; line-height: 17px; font-weight: 800; text-align: center;
  }
</style>
</head>
<body>

<div class="version-title v1">VERSION 1: LABEL ONLY</div>

<section class="label v1">
  <div class="brand">
    <div class="brand-row"><span class="brand-dot"></span><span class="brand-name">Vela Drug Tests</span></div>
  </div>
  <div class="divider"></div>
  <div class="patient-heading">PATIENT INFORMATION</div>
  <div class="field name">Name:<span class="line"></span></div>
  <div class="field dob">Date of Birth:<span class="line"></span></div>
  <div class="field date">Date:<span class="line"></span></div>
  <div class="field time">Time:<span class="line"></span></div>
  <div class="field temp">Temp℃:<span class="line"></span></div>
  <div class="field specimen">Specimen ID:<span class="line"></span></div>
  <div class="footer-rule"></div>
  <div class="ref-box">REF</div>
  <div class="product-label">PRODUCT CODE:</div>
  <div class="product-code">TUB-47</div>
  <svg class="ivd-icon" viewBox="0 0 31 31"><circle cx="15.5" cy="15.5" r="14" fill="none" stroke="#0f2b5b" stroke-width="1.6"/></svg>
  <div class="ivd-text">For In Vitro Diagnostic Use<br>Not For Internal Use</div>
  <div class="volume-panel">
    <svg width="60" height="240" viewBox="0 0 60 240" stroke="#0f2b5b" stroke-width="1.3">
      <line x1="14" y1="25" x2="47" y2="25" stroke-width="2"/>
      <line x1="14" y1="39" x2="31" y2="39"/><line x1="14" y1="53" x2="31" y2="53"/>
      <line x1="14" y1="67" x2="31" y2="67"/><line x1="14" y1="81" x2="31" y2="81"/>
      <line x1="14" y1="95" x2="47" y2="95" stroke-width="2"/>
      <line x1="14" y1="109" x2="31" y2="109"/><line x1="14" y1="124" x2="31" y2="124"/>
      <line x1="14" y1="138" x2="31" y2="138"/><line x1="14" y1="152" x2="31" y2="152"/>
      <line x1="14" y1="166" x2="47" y2="166" stroke-width="2"/>
    </svg>
    <div class="vol v90">90 <small>mL</small></div>
    <div class="vol v60">60 <small>mL</small></div>
    <div class="vol v30">30 <small>mL</small></div>
  </div>
</section>

<div class="version-title v2">VERSION 2: LABEL WITH STERILE SEAL</div>

<section class="label v2">
  <div class="brand">
    <div class="brand-row"><span class="brand-dot"></span><span class="brand-name">Vela Drug Tests</span></div>
  </div>
  <div class="divider"></div>
  <div class="patient-heading">PATIENT INFORMATION</div>
  <div class="field name">Name:<span class="line"></span></div>
  <div class="field dob">Date of Birth:<span class="line"></span></div>
  <div class="field date">Date:<span class="line"></span></div>
  <div class="field time">Time:<span class="line"></span></div>
  <div class="field temp">Temp℃:<span class="line"></span></div>
  <div class="field specimen">Specimen ID:<span class="line"></span></div>
  <div class="footer-rule"></div>
  <div class="ref-box">REF</div>
  <div class="product-label">PRODUCT CODE:</div>
  <div class="product-code">TUB-47</div>
  <svg class="ivd-icon" viewBox="0 0 31 31"><circle cx="15.5" cy="15.5" r="14" fill="none" stroke="#0f2b5b" stroke-width="1.6"/></svg>
  <div class="ivd-text">For In Vitro Diagnostic Use<br>Not For Internal Use</div>
  <div class="volume-panel">
    <svg width="60" height="240" viewBox="0 0 60 240" stroke="#0f2b5b" stroke-width="1.3">
      <line x1="17" y1="25" x2="50" y2="25" stroke-width="2"/>
      <line x1="17" y1="39" x2="34" y2="39"/><line x1="17" y1="53" x2="34" y2="53"/>
      <line x1="17" y1="67" x2="34" y2="67"/><line x1="17" y1="81" x2="34" y2="81"/>
      <line x1="17" y1="95" x2="50" y2="95" stroke-width="2"/>
      <line x1="17" y1="109" x2="34" y2="109"/><line x1="17" y1="124" x2="34" y2="124"/>
      <line x1="17" y1="138" x2="34" y2="138"/><line x1="17" y1="152" x2="34" y2="152"/>
      <line x1="17" y1="166" x2="50" y2="166" stroke-width="2"/>
    </svg>
    <div class="vol v90">90 <small>mL</small></div>
    <div class="vol v60">60 <small>mL</small></div>
    <div class="vol v30">30 <small>mL</small></div>
  </div>
</section>

<aside class="seal">
  <svg class="seal-icon shield" viewBox="0 0 31 31">
    <path d="M15.5 2 L27 6 V14 C27 21 22 26.5 15.5 29 C9 26.5 4 21 4 14 V6 Z" fill="none" stroke="#fff" stroke-width="2"/>
    <rect x="13.3" y="8.5" width="4.4" height="13" fill="#fff"/>
    <rect x="9" y="12.8" width="13" height="4.4" fill="#fff"/>
  </svg>
  <div class="seal-word sterile">STERILE</div>
  <div class="seal-band">
    <svg width="81" height="176" viewBox="0 0 81 176" fill="#0f2b5b">
      <path d="M40.5 7 L45 16 H36 Z"/>
      <path d="M40.5 169 L45 160 H36 Z"/>
    </svg>
    <div class="seal-warning">DO NOT USE IF<br>SEAL IS BROKEN</div>
  </div>
  <svg class="seal-icon lock" viewBox="0 0 31 31">
    <path d="M10 14 V10 a5.5 5.5 0 0 1 11 0 V14" fill="none" stroke="#fff" stroke-width="2.4"/>
    <rect x="7" y="14" width="17" height="13" rx="2" fill="#fff"/>
    <circle cx="15.5" cy="20" r="2" fill="#0f2b5b"/>
  </svg>
  <div class="seal-word tamper">TAMPER<br>EVIDENT</div>
</aside>

</body>
</html>
```